The Lantern Makers Guild Presents: A Halloween Soiree

Halloween Invite text:
You are cordially invited
to honor the Ghosts of Startups Past
Date: Halloween Proper, Tuesday, October 31
Place: Spook Junction, 71-73 West 52nd St, 5th FL, doors to the right of Wrenfield, between Lexhill and Marlowe.
Time: 7-9 pm
Costumes: Optional, but rewarded with prizes
Food: light bites and beer
Rules of enghoulment: Come dressed as your favorite failed startup. Or, at least wear a name tag with the company's name. Be prepared to discuss why the startup failed and what can be learned from it.
Updates
The deadline is extended till tomorrow morning, NY time. thanks! Added Tuesday, October 3, 2017
Target Market(s)
Founder, tech CEOs of small startups
Industry/Entity Type
Tech
Requirements
Must have
- Design Must include logos of the following failed startups:
- cartloop.example
- zimbit.example
- KOV.example
- toyvane.example
- furly.example
- yem.example
- Please be creative about the way you present the logos. Maybe they should look like ghosts. Or are on tombstones or something.

```html
<!DOCTYPE html>
<html lang="en">
<head>
<meta charset="utf-8">
<title>The Ghosts of Startups Past – Halloween Invitation</title>
<link rel="stylesheet" href="https://fonts.googleapis.com/css2?family=IM+Fell+English&family=Cormorant+Garamond:ital,wght@1,500&family=Open+Sans:wght@400;700&display=swap">
<style>
  :root {
    --page: #ffffff;
    --ink-light: #f4f1ea;
    --accent: #f0923a;
    --ghost-logo: rgba(150, 150, 150, 0.55);
    --night-top: #3a3a3d;
    --night-mid: #1c1c1e;
    --night-deep: #050505;
    --pumpkin-glow: rgba(214, 104, 36, 0.55);
  }
  html, body {
    margin: 0;
    padding: 0;
    width: 1200px;
    height: 1200px;
    overflow: hidden;
    background: var(--page);
  }
  .invitation {
    position: absolute;
    left: 273px;
    top: 137px;
    width: 657px;
    height: 919px;
    overflow: hidden;
    color: var(--ink-light);
    font-family: "IM Fell English", Georgia, serif;
  }
  .invitation__backdrop {
    position: absolute;
    inset: 0;
    background:
      radial-gradient(ellipse 90px 120px at 40px 300px, var(--pumpkin-glow), transparent 70%),
      radial-gradient(ellipse 110px 140px at 610px 300px, var(--pumpkin-glow), transparent 70%),
      radial-gradient(ellipse 200px 160px at 330px 150px, rgba(120,120,125,0.35), transparent 75%),
      linear-gradient(180deg, var(--night-top) 0%, var(--night-mid) 45%, #2b2b2e 62%, var(--night-mid) 78%, var(--night-deep) 100%);
  }
  .invitation__lead {
    position: absolute;
    top: 78px;
    left: 0;
    right: 0;
    margin: 0;
    text-align: center;
    font-family: "Cormorant Garamond", Georgia, serif;
    font-style: italic;
    font-weight: 500;
    font-size: 24px;
    letter-spacing: 0.4px;
  }
  .title {
    position: absolute;
    left: 0;
    right: 0;
    top: 0;
    margin: 0;
    font-weight: 400;
    line-height: 1;
  }
  .title span { position: absolute; white-space: nowrap; }
  .title__the { left: 288px; top: 266px; font-size: 50px; }
  .title__ghosts { left: 190px; top: 282px; font-size: 96px; }
  .title__of { left: 158px; top: 399px; font-size: 42px; }
  .title__startups { left: 205px; top: 354px; font-size: 96px; }
  .title__past { left: 255px; top: 422px; font-size: 96px; }
  .ghost-logos { position: absolute; inset: 0; }
  .ghost-logo {
    position: absolute;
    transform: translate(-50%, -50%);
    font-family: "Open Sans", Arial, sans-serif;
    font-weight: 700;
    font-size: 19px;
    color: var(--ghost-logo);
    white-space: nowrap;
  }
  .details {
    position: absolute;
    top: 670px;
    left: 0;
    right: 0;
    margin: 0;
    text-align: center;
    font-size: 21px;
    letter-spacing: 0.6px;
    line-height: 27.5px;
    white-space: nowrap;
  }
  .details__value { color: var(--accent); }
  .rules {
    position: absolute;
    top: 826px;
    left: 58px;
    right: 40px;
    margin: 0;
    font-family: "Open Sans", Arial, sans-serif;
    font-size: 11px;
    line-height: 20px;
    white-space: nowrap;
  }
  .rules strong { font-weight: 700; }
</style>
</head>
<body>
  <main class="invitation">
    <div class="invitation__backdrop" role="img" aria-label="Dark misty Halloween photograph: hands holding an animal skull, pumpkins, lit candles and tangled roots in smoke"></div>

    <p class="invitation__lead">You are cordially invited to honor</p>

    <h1 class="title" aria-label="The Ghosts of Startups Past">
      <span class="title__the">The</span>
      <span class="title__ghosts">Ghosts</span>
      <span class="title__of">of</span>
      <span class="title__startups">Startups</span>
      <span class="title__past">Past</span>
    </h1>

    <div class="ghost-logos">
      <span class="ghost-logo" style="left:115px; top:547px;">toyvane.example</span>
      <span class="ghost-logo" style="left:527px; top:523px;">furly.example</span>
      <span class="ghost-logo" style="left:297px; top:571px;">cartloop.example</span>
      <span class="ghost-logo" style="left:560px; top:579px;">KOV.example</span>
      <span class="ghost-logo" style="left:150px; top:617px;">yem.example</span>
      <span class="ghost-logo" style="left:399px; top:619px;">zimbit.example</span>
    </div>

    <p class="details">
      Date: <span class="details__value">Halloween Proper, Tuesday, October 31</span><br>
      Place: <span class="details__value">Spook Junction, 71-73 West 52nd St, 5th FL,</span><br>
      <span class="details__value">doors to the right of Wrenfield, between Lexhill and Marlowe.</span><br>
      Time: <span class="details__value">7-9 pm</span> Costumes: <span class="details__value">Optional, but rewarded with prizes</span><br>
      Food: <span class="details__value">Light bites and beer</span>
    </p>

    <p class="rules"><strong>Rules of enghoulment:</strong>&nbsp; Come dressed as your favorite failed startup. Or, at least wear a name tag<br>with the company's name. Be prepared to discuss why the startup failed and what can be learned from it.</p>
  </main>
</body>
</html>
```